Birchline Flooring Supply

Basic one-sided business card design using the attached logo. Vintage americana theme. Font is modified Arial Nova Cond, but anything that coordinates can be used

```html
<!DOCTYPE html>
<html lang="en">
<head>
<meta charset="utf-8">
<title>Birchline Flooring Supply – Business Card</title>
<link rel="stylesheet" href="https://fonts.googleapis.com/css2?family=Lato:wght@400;700&display=swap">
<style>
  :root {
    --page-bg: #e9e4dc;
    --card-bg: #050505;
    --tan: #b8987a;
    --ink-light: #f4f1ec;
  }
  html, body {
    margin: 0;
    width: 1200px;
    height: 931px;
    overflow: hidden;
    background: var(--page-bg);
  }
  .canvas {
    width: 1200px;
    height: 931px;
    display: flex;
    flex-direction: column;
    align-items: center;
    justify-content: center;
    gap: 36px;
  }
  .business-card {
    position: relative;
    width: 720px;
    height: 412px;
    background: var(--card-bg);
    border-radius: 24px;
    box-shadow: 0 14px 32px rgba(0,0,0,0.28);
    font-family: "Lato", sans-serif;
    color: var(--ink-light);
    overflow: hidden;
  }
  .brand {
    display: flex;
    align-items: center;
    gap: 14px;
  }
  .brand-dot {
    flex: none;
    border-radius: 50%;
    background: var(--tan);
  }
  .brand-name {
    margin: 0;
    font-weight: 700;
    line-height: 1.15;
    color: var(--ink-light);
  }

  /* Front side */
  .card-front .brand {
    position: absolute;
    inset: 0;
    justify-content: center;
  }
  .card-front .brand-dot { width: 24px; height: 24px; }
  .card-front .brand-name { font-size: 40px; }

  /* Back side */
  .card-back .brand {
    position: absolute;
    left: 40px;
    top: 0;
    width: 300px;
    height: 412px;
    justify-content: center;
  }
  .card-back .brand-dot { width: 18px; height: 18px; }
  .card-back .brand-name { font-size: 28px; }
  .divider {
    position: absolute;
    left: 372px;
    top: 70px;
    width: 2px;
    height: 272px;
    background: linear-gradient(to bottom, rgba(184,152,122,0), var(--tan) 25%, var(--tan) 75%, rgba(184,152,122,0));
  }
  .contact {
    position: absolute;
    left: 410px;
    top: 92px;
    width: 290px;
  }
  .person-name {
    margin: 0;
    font-weight: 700;
    font-size: 27px;
    letter-spacing: 0.3px;
    text-transform: uppercase;
    color: var(--tan);
  }
  .person-role {
    margin: 2px 0 22px;
    font-size: 17px;
  }
  .contact-list {
    list-style: none;
    margin: 0 0 20px;
    padding: 0;
  }
  .contact-item {
    display: flex;
    align-items: center;
    gap: 14px;
    font-size: 17px;
    height: 29px;
  }
  .contact-icon {
    flex: none;
    width: 19px;
    height: 19px;
    fill: var(--tan);
  }
  .address {
    margin: 0;
    font-size: 17px;
    line-height: 1.4;
    font-style: normal;
  }
</style>
</head>
<body>
<main class="canvas">
  <section class="business-card card-front">
    <div class="brand">
      <span class="brand-dot"></span>
      <h1 class="brand-name">Birchline<br>Flooring Supply</h1>
    </div>
  </section>

  <section class="business-card card-back">
    <div class="brand">
      <span class="brand-dot"></span>
      <h2 class="brand-name">Birchline<br>Flooring Supply</h2>
    </div>

    <div class="divider"></div>

    <div class="contact">
      <h3 class="person-name">Daniel Harlow</h3>
      <p class="person-role">Managing Director</p>
      <ul class="contact-list">
        <li class="contact-item">
          <svg class="contact-icon" viewBox="0 0 24 24" aria-hidden="true"><path d="M6.6 10.8a15.1 15.1 0 0 0 6.6 6.6l2.2-2.2a1 1 0 0 1 1-.25 11.4 11.4 0 0 0 3.6.57 1 1 0 0 1 1 1V20a1 1 0 0 1-1 1A17 17 0 0 1 3 4a1 1 0 0 1 1-1h3.5a1 1 0 0 1 1 1c0 1.25.2 2.45.57 3.57a1 1 0 0 1-.25 1z"/></svg>
          <span>055-318 624 907</span>
        </li>
        <li class="contact-item">
          <svg class="contact-icon" viewBox="0 0 24 24" aria-hidden="true"><path d="M2 5h20v14H2z"/><path d="M2 5l10 8 10-8" fill="none" stroke="#050505" stroke-width="1.6"/></svg>
          <span>hello@birchlinefs.com</span>
        </li>
        <li class="contact-item">
          <svg class="contact-icon" viewBox="0 0 24 24" aria-hidden="true"><circle cx="12" cy="12" r="9" fill="none" stroke="#b8987a" stroke-width="2"/><path d="M3 12h18M12 3c3 3 3 15 0 18M12 3c-3 3-3 15 0 18" fill="none" stroke="#b8987a" stroke-width="1.6"/></svg>
          <span>www.birchlinefs.com</span>
        </li>
      </ul>
      <address class="address">218, Timber Row Avenue<br>60417, Riverton</address>
    </div>
  </section>
</main>
</body>
</html>
```